Website for boutique digital agency helping high-tech startups accelerate growth.

We need a website design for a relatively young company based in Mauritius called 'LumaTrel'.

We are a professional services firm delivering digital infrastructure for revenue operations (RevOps)*.

Entrepreneurial startups and SMBs in the technology sector work with us to accelerate growth by delivering extraordinary customer experiences across the full customer lifecycle.

We would like a colourful design that utilises the (4) colours of our existing logo design.

The final design should communicate dynamic growth through relentless customer focus.
----------------------------------------------------------
*Revenue Operations (RevOps) is the strategic alignment of sales, marketing and customer success operations to accelerate growth by delivering extraordinary customer experiences across the full customer life cycle.

Target Market(s)

Entrepreneurial startups and SMBs (Small/Medium Businesses) in the technology sector.

Question: Why the technology sector?

Answer: Because technology entrepreneurs often have a tremendous challenge to effectively communicate to the market and to prospective customers the value and the benefits of their products & services due to the inherent complexity of technological innovation.

LumaTrel is a team of creatively-minded engineers and technologists who have worked with and understand the technologies and innovations our clients are passionate about bringing to market.

Industry/Entity Type

Professional Service

Number of Pages Required

5+ page

Font styles to use
Sans Serif

Requirements
Must have
• Minimalistic designs rich with visual meaning are highly preferred. Mobile responsive designs are also required. Must show how designs render on Desktop, Tablet and Smartphone devices.

Website pages:
1) Homepage: problem statement, target customers, value proposition & benefits
2) Services: 3-4 tiers of services packages with pricing and "how to work with us"
3) Resources: links to all kinds of relevant materials
4) Contact Us: contact form and special project quote form
5) Blog: matrix design with featured images for each post
Nice to have
• Bold, interesting, colourful, inspiring images that visually communicate:
- relentless customer focus
- extraordinary, memorable experiences
- business at the speed of innovation
Should not have
• Any meme or theme that panders to "political correctness".

```html
<!DOCTYPE html>
<html lang="en">
<head>
<meta charset="utf-8">
<title>LumaTrel — Boutique Digital Agency</title>
<link href="https://fonts.googleapis.com/css2?family=Poppins:wght@400;500;600;700;800&display=swap" rel="stylesheet">
<style>
:root{
  --red:#fe0037;
  --green:#84c52a;
  --teal:#1f8a85;
  --teal-dark:#17716d;
  --ink:#222327;
  --text:#6b6b6b;
  --grey-bg:#f3f3f3;
  --footer:#1f2023;
  --white:#ffffff;
}
*{box-sizing:border-box;margin:0;padding:0}
html,body{width:1200px;height:4574px;overflow:hidden;background:var(--white)}
body{font-family:"Poppins",sans-serif;color:var(--ink)}
.canvas{position:relative;width:1200px;height:4574px;overflow:hidden}
.abs{position:absolute}
.bg-shape{position:absolute;left:0;top:0;width:1200px;height:4574px}

/* header */
.social{display:flex;gap:12px}
.social span{width:22px;height:22px;border-radius:50%;background:var(--red);display:block}
.social.white span{background:var(--white)}
.brand{font-weight:700;font-size:31px;color:#3a3a3a;letter-spacing:.5px}
.brand-dot{width:54px;height:54px;border-radius:50%;background:var(--red);margin:0 auto 8px}
.nav a{position:absolute;font-size:11px;font-weight:600;color:#222;text-decoration:none;letter-spacing:.3px}
.nav a.active{color:var(--red)}
.phone{display:flex;align-items:center;gap:12px;font-size:12px;font-weight:500}

/* hero */
.hero-photo{left:0;top:160px;width:1200px;height:610px;background:linear-gradient(100deg,#5c7c7a 0%,#7f9a95 45%,#b89a84 70%,#8a7e72 100%)}
.hero-kicker{left:172px;top:355px;color:var(--white);font-weight:700;font-size:31px}
.hero-title{left:170px;top:395px;color:var(--white);font-weight:800;font-size:60px;letter-spacing:.5px}
.hero-text{left:173px;top:478px;width:470px;color:var(--white);font-size:11.5px;line-height:22px}
.arrow{font-size:26px;font-weight:400;color:var(--white)}
.diamond{left:568px;top:730px;width:64px;height:64px;background:var(--white);transform:rotate(45deg);box-shadow:0 3px 10px rgba(0,0,0,.15)}
.diamond i{position:absolute;left:22px;top:22px;width:20px;height:20px;border-radius:50%;background:var(--red)}
.feature{width:300px;text-align:center;color:var(--white)}
.feature svg{display:block;margin:0 auto 20px}
.feature h3{font-weight:500;font-size:21px;margin-bottom:18px}
.feature p{font-size:11.5px;line-height:23px}

/* section titles */
.label{font-weight:700;font-size:20px;color:var(--red);letter-spacing:.3px}
.title{font-weight:800;font-size:46px;color:var(--ink);line-height:1}
.body-text{font-size:11.5px;line-height:23px;color:var(--text)}
.btn-outline{display:flex;align-items:center;justify-content:center;font-size:11px;font-weight:600;border:2px solid var(--red);color:var(--red)}

/* about */
.about-photo{left:179px;top:1195px;width:375px;height:335px;background:linear-gradient(160deg,#9aa3a8,#5f6a70 60%,#3e4750);clip-path:polygon(0 11%,100% 0,100% 100%,0 100%)}
.photo-caption{position:absolute;left:0;bottom:0;width:100%;height:80px;background:rgba(132,197,42,.92);color:var(--white);font-size:11.5px;line-height:22px;padding:16px 38px}

/* team */
.member{width:254px}
.member .photo{width:254px;height:229px;background:linear-gradient(140deg,#b7b9bb,#6f7478 55%,#3c4046)}
.member h4{font-weight:500;font-size:21px;margin:26px 0 12px}
.member .social{margin-top:14px}

/* packages */
.pkg{width:254px;height:486px;background:var(--white);box-shadow:0 4px 18px rgba(0,0,0,.1)}
.pkg-head{height:114px;color:var(--white);text-align:center;padding-top:55px;clip-path:polygon(0 0,100% 14%,100% 100%,0 100%)}
.pkg-head.flip{clip-path:polygon(0 14%,100% 0,100% 100%,0 100%)}
.pkg-head b{display:block;font-size:21px;font-weight:700;line-height:1}
.pkg-head small{font-size:9.5px;font-weight:600;letter-spacing:1px}
.price{text-align:center;margin-top:22px;font-size:44px;font-weight:600;color:var(--ink);line-height:1}
.price sup{font-size:20px;font-weight:400;vertical-align:top}
.price span{font-size:21px;font-weight:400;color:var(--text)}
.pkg ul{list-style:none;margin:18px 0 0 42px}
.pkg li{display:flex;align-items:center;gap:12px;font-size:11.5px;color:var(--text);height:38px}
.tick{width:15px;height:15px;border-radius:50%;border:1.6px solid currentColor;position:relative;flex:none}
.tick:after{content:"";position:absolute;left:4px;top:1.5px;width:3.5px;height:7px;border:solid currentColor;border-width:0 1.6px 1.6px 0;transform:rotate(45deg)}
.pkg .select{display:block;width:139px;height:43px;margin:20px auto 0;color:var(--white);font-size:11px;font-weight:600;text-align:center;line-height:43px}
.ribbon{position:absolute;left:8px;top:24px;width:90px;height:17px;background:var(--white);color:var(--red);font-size:8px;font-weight:700;text-align:center;line-height:17px;transform:rotate(-38deg);transform-origin:left top}

/* benefits */
.city{left:0;top:3200px;width:260px;height:496px;background:linear-gradient(180deg,rgba(255,255,255,0) 0%,rgba(10,70,68,.35) 100%)}
.benefits li{display:flex;align-items:center;gap:14px;color:var(--white);font-size:11.5px;height:38px;list-style:none}
.benefit-photo{left:666px;top:3257px;width:372px;height:337px;background:linear-gradient(120deg,#e9eef0,#c8d0d3 55%,#8e979c);clip-path:polygon(0 0,100% 9%,100% 100%,0 100%)}

/* testimonial */
.avatar{left:563px;top:3884px;width:74px;height:74px;border-radius:50%;background:linear-gradient(150deg,#d8b59e,#8f6a57)}

/* footer */
.footer-nav a{position:absolute;font-size:11px;font-weight:500;color:#9a9a9a;text-decoration:none}
.footer-nav a.active{color:var(--white)}
</style>
</head>
<body>
<div class="canvas">

  <!-- background bands -->
  <svg class="bg-shape" viewBox="0 0 1200 4574" aria-hidden="true">
    <polygon points="0,1603 1200,1731 1200,2331 0,2331" fill="#f3f3f3"/>
    <polygon points="0,3209 600,3145 1200,3209 1200,3696 0,3696" fill="#1f8a85"/>
    <polygon points="0,4129 600,4171 1200,4129 1200,4574 0,4574" fill="#1f2023"/>
  </svg>

  <!-- header -->
  <header>
    <div class="abs social" style="left:184px;top:44px"><span></span><span></span><span></span></div>
    <div class="abs" style="left:500px;top:30px;width:200px;text-align:center">
      <div class="brand-dot"></div>
      <div class="brand">lumatrel.io</div>
    </div>
    <div class="abs phone" style="left:915px;top:44px">
      <svg width="22" height="22" viewBox="0 0 24 24"><path d="M6.6 10.8c1.4 2.8 3.8 5.1 6.6 6.6l2.2-2.2c.3-.3.7-.4 1-.2 1.1.4 2.3.6 3.6.6.6 0 1 .4 1 1V20c0 .6-.4 1-1 1C10.6 21 3 13.4 3 4c0-.6.4-1 1-1h3.5c.6 0 1 .4 1 1 0 1.3.2 2.5.6 3.6.1.3 0 .7-.2 1z" fill="#fe0037"/></svg>
      (123) 555-0147
    </div>
    <nav class="nav">
      <a class="active" href="#" style="left:187px;top:112px">HOME</a>
      <a href="#" style="left:281px;top:112px">ABOUT</a>
      <a href="#" style="left:384px;top:112px">SERVICES</a>
      <a href="#" style="left:773px;top:112px">RESOURCES</a>
      <a href="#" style="left:905px;top:112px">BLOG</a>
      <a href="#" style="left:989px;top:112px">CONTACT</a>
    </nav>
  </header>

  <!-- hero -->
  <section class="hero">
    <div class="abs hero-photo" role="img" aria-label="Smiling businesswoman portrait in an office"></div>
    <div class="abs hero-kicker">BOUTIQUE</div>
    <div class="abs hero-title">DIGITAL AGENCY</div>
    <p class="abs hero-text">We are a professional services firm delivering digital infrastructure for revenue operations (RevOps)*. Entrepreneurial startups.</p>
    <div class="abs arrow" style="left:994px;top:432px">&#8249;</div>
    <div class="abs arrow" style="left:1027px;top:432px">&#8250;</div>

    <svg class="abs" style="left:0;top:700px" width="1200" height="385" viewBox="0 0 1200 385" aria-hidden="true">
      <polygon points="0,5 600,70 1200,5 1200,385 0,385" fill="#fe0037"/>
    </svg>
    <div class="abs diamond"><i></i></div>

    <div class="abs feature" style="left:109px;top:836px">
      <svg width="60" height="60" viewBox="0 0 60 60" fill="none" stroke="#fff" stroke-width="2"><circle cx="26" cy="22" r="14"/><path d="M26 8v14h14M4 56h52M10 56V44M18 56V38M26 56V42M34 56V36M42 56V40M50 56V32"/></svg>
      <h3>Problem statement</h3>
      <p>Entrepreneurial startups and SMBs in the technology sector work</p>
    </div>
    <div class="abs feature" style="left:451px;top:836px">
      <svg width="60" height="60" viewBox="0 0 60 60" fill="none" stroke="#fff" stroke-width="2"><path d="M6 56h48M10 56V40h8v16M24 56V32h8v16M38 56V24h8v32M20 22l10-10 8 6 14-14M44 4h8v8"/></svg>
      <h3>Value proposition &amp; benefits</h3>
      <p>Entrepreneurial startups and SMBs in the technology sector work with us to accelerate</p>
    </div>
    <div class="abs feature" style="left:796px;top:836px">
      <svg width="60" height="60" viewBox="0 0 60 60" fill="none" stroke="#fff" stroke-width="2"><circle cx="30" cy="30" r="8"/><circle cx="12" cy="12" r="6"/><circle cx="48" cy="12" r="6"/><circle cx="12" cy="48" r="6"/><circle cx="48" cy="48" r="6"/><path d="M17 17l7 7M43 17l-7 7M17 43l7-7M43 43l-7-7"/></svg>
      <h3>Target customers</h3>
      <p>SMBs in the technology sector work with us to accelerate growth by delivering</p>
    </div>
  </section>

  <!-- about -->
  <section class="about">
    <div class="abs about-photo" role="img" aria-label="Confident businesswoman standing in front of her team on office stairs">
      <div class="photo-caption">SMBs in the technology sector work with us to accelerate growth by delivering</div>
    </div>
    <div class="abs label" style="left:625px;top:1223px">DIGITAL AGENCY</div>
    <h2 class="abs title" style="left:622px;top:1253px">ABOUT US</h2>
    <p class="abs body-text" style="left:625px;top:1320px;width:420px">We are a professional services firm delivering digital infrastructure for revenue operations (RevOps)*.</p>
    <p class="abs body-text" style="left:625px;top:1387px;width:420px">Entrepreneurial startups and SMBs in the technology sector work with us to accelerate growth by delivering extraordinary customer experiences across the full customer lifecycle.</p>
    <div class="abs btn-outline" style="left:625px;top:1488px;width:140px;height:42px">VIEW MORE</div>
  </section>

  <!-- team -->
  <section class="team">
    <div class="abs label" style="left:178px;top:1745px">DIGITAL AGENCY</div>
    <h2 class="abs title" style="left:176px;top:1775px">LUMATREL TEAM</h2>
    <div class="abs arrow" style="left:990px;top:1785px;color:#222">&#8249;</div>
    <div class="abs arrow" style="left:1023px;top:1785px;color:#222">&#8250;</div>

    <div class="abs member" style="left:179px;top:1869px">
      <div class="photo" role="img" aria-label="Team member portrait in office"></div>
      <h4>Name Here</h4>
      <p class="body-text">Entrepreneurial startups and SMBs in the technology sector work</p>
      <div class="social"><span></span><span></span><span></span></div>
    </div>
    <div class="abs member" style="left:479px;top:1869px">
      <div class="photo" role="img" aria-label="Team member portrait in office"></div>
      <h4>Name Here</h4>
      <p class="body-text">Entrepreneurial startups and SMBs in the technology sector work</p>
      <div class="social"><span></span><span></span><span></span></div>
    </div>
    <div class="abs member" style="left:779px;top:1869px">
      <div class="photo" role="img" aria-label="Team member portrait on office stairs"></div>
      <h4>Name Here</h4>
      <p class="body-text">Entrepreneurial startups and SMBs in the technology sector work</p>
      <div class="social"><span></span><span></span><span></span></div>
    </div>
  </section>

  <!-- packages -->
  <section class="packages">
    <div class="abs label" style="left:0;top:2407px;width:1200px;text-align:center">DIGITAL AGENCY</div>
    <h2 class="abs title" style="left:0;top:2437px;width:1200px;text-align:center">OUR PACKAGES</h2>

    <div class="abs pkg" style="left:179px;top:2549px;color:var(--green)">
      <div class="pkg-head" style="background:var(--green)"><b>STANDARD</b><small>PACKAGE</small></div>
      <div class="price"><sup>$</sup>19<span>/month</span></div>
      <ul>
        <li><i class="tick"></i>Entrepreneurial startups</li>
        <li><i class="tick"></i>SMBs in the technology</li>
        <li><i class="tick"></i>Sector work with us to</li>
        <li><i class="tick"></i>Accelerate growth by</li>
        <li><i class="tick"></i>Delivering extraordinary</li>
      </ul>
      <div class="select" style="background:var(--green)">SELECT</div>
    </div>

    <div class="abs pkg" style="left:479px;top:2549px;color:var(--red)">
      <div class="pkg-head" style="background:var(--red);position:relative"><b>PREMIUM</b><small>PACKAGE</small><div class="ribbon">PREMIUM</div></div>
      <div class="price"><sup>$</sup>89<span>/month</span></div>
      <ul>
        <li><i class="tick"></i>Entrepreneurial startups</li>
        <li><i class="tick"></i>SMBs in the technology</li>
        <li><i class="tick"></i>Sector work with us to</li>
        <li><i class="tick"></i>Accelerate growth by</li>
        <li><i class="tick"></i>Delivering extraordinary</li>
      </ul>
      <div class="select" style="background:var(--red)">SELECT</div>
    </div>

    <div class="abs pkg" style="left:779px;top:2549px;color:var(--teal)">
      <div class="pkg-head flip" style="background:var(--teal)"><b>BUSINESS</b><small>PACKAGE</small></div>
      <div class="price"><sup>$</sup>39<span>/month</span></div>
      <ul>
        <li><i class="tick"></i>Entrepreneurial startups</li>
        <li><i class="tick"></i>SMBs in the technology</li>
        <li><i class="tick"></i>Sector work with us to</li>
        <li><i class="tick"></i>Accelerate growth by</li>
        <li><i class="tick"></i>Delivering extraordinary</li>
      </ul>
      <div class="select" style="background:var(--teal)">SELECT</div>
    </div>
  </section>

  <!-- benefits -->
  <section class="benefits">
    <div class="abs city" role="img" aria-label="Faint city skyline behind the section"></div>
    <div class="abs label" style="left:180px;top:3284px;color:var(--white)">DIGITAL AGENCY</div>
    <h2 class="abs title" style="left:177px;top:3314px;color:var(--white)">OUR BENEFITS</h2>
    <ul class="abs" style="left:180px;top:3378px">
      <li><i class="tick"></i>Entrepreneurial startups and SMBs in the</li>
      <li><i class="tick"></i>Technology sector work with us to accelerate</li>
      <li><i class="tick"></i>Growth by delivering extraordinary customer</li>
      <li><i class="tick"></i>Experiences across the full customer lifecycle.</li>
    </ul>
    <div class="abs btn-outline" style="left:176px;top:3550px;width:138px;height:43px;border-color:var(--white);color:var(--white)">VIEW MORE</div>
    <div class="abs benefit-photo" role="img" aria-label="Hand holding a smartphone showing a sales dashboard">
      <div class="photo-caption" style="height:83px;padding:18px 36px">Entrepreneurial startups and SMBs in the technology sector work with</div>
    </div>
  </section>

  <!-- prospective customers -->
  <section class="testimonial">
    <h2 class="abs title" style="left:0;top:3800px;width:1200px;text-align:center">PROSPECTIVE CUSTOMERS</h2>
    <div class="abs arrow" style="left:514px;top:3903px;color:#222">&#8249;</div>
    <div class="abs avatar" role="img" aria-label="Customer portrait"></div>
    <div class="abs arrow" style="left:675px;top:3903px;color:#222">&#8250;</div>
    <p class="abs body-text" style="left:180px;top:3998px;width:840px;text-align:center">Technology entrepreneurs often have a tremendous challenge to effectively communicate to the market and to prospective customers the value and the benefits of their products &amp; services due to the inherent complexity of technological innovation.</p>
    <div class="abs" style="left:0;top:4068px;width:1200px;text-align:center;color:var(--red);font-size:21px;font-weight:500">Name Here</div>
  </section>

  <!-- footer -->
  <footer>
    <div class="abs" style="left:158px;top:4338px;color:var(--white);font-size:21px;font-weight:400">Contact Us</div>
    <div class="abs" style="left:158px;top:4393px;display:flex;align-items:center;gap:10px;color:#9a9a9a;font-size:11.5px">
      <svg width="14" height="14" viewBox="0 0 24 24"><path d="M6.6 10.8c1.4 2.8 3.8 5.1 6.6 6.6l2.2-2.2c.3-.3.7-.4 1-.2 1.1.4 2.3.6 3.6.6.6 0 1 .4 1 1V20c0 .6-.4 1-1 1C10.6 21 3 13.4 3 4c0-.6.4-1 1-1h3.5c.6 0 1 .4 1 1 0 1.3.2 2.5.6 3.6.1.3 0 .7-.2 1z" fill="#fff"/></svg>
      (123) 555-0147
    </div>
    <div class="abs" style="left:158px;top:4423px;display:flex;align-items:center;gap:10px;color:var(--white);font-size:11.5px">
      <svg width="15" height="11" viewBox="0 0 15 11" fill="none" stroke="#fff" stroke-width="1.4"><rect x=".7" y=".7" width="13.6" height="9.6"/><path d="M.7 .7l6.8 5.6 6.8-5.6"/></svg>
      info@lumatrel.io
    </div>
    <div class="abs" style="left:500px;top:4285px;width:200px;text-align:center">
      <div class="brand-dot"></div>
      <div class="brand" style="color:var(--white)">lumatrel.io</div>
    </div>
    <div class="abs social white" style="left:549px;top:4405px"><span></span><span></span><span></span></div>
    <div class="abs" style="left:0;top:4452px;width:1200px;text-align:center;font-size:11px;color:#9a9a9a">Copyright © 2020 <span style="color:var(--white)">LumaTrel.io</span></div>
    <nav class="footer-nav">
      <a class="active" href="#" style="left:852px;top:4345px">HOME</a>
      <a href="#" style="left:943px;top:4345px">BLOG</a>
      <a href="#" style="left:852px;top:4374px">ABOUT</a>
      <a href="#" style="left:943px;top:4374px">CONTACT</a>
      <a href="#" style="left:852px;top:4403px">SERVICES</a>
      <a href="#" style="left:852px;top:4431px">RESOURCES</a>
    </nav>
  </footer>

</div>
</body>
</html>
```